General Contractors need a new Crisp updated Card Design

We need a new business card design for our company of 25 years based in Toronto call Holvaster Building Inc. : Our goal is to be the leading commercial contractors in Toronto by providing exceptional value to our clients. We work very hard to deliver professional, quality, service in conjunction with consistent price competitiveness to all of our clients on every single project.

Target Market(s)

Design & Build Clients

Industry/Entity Type

Construction Company

Contact Information for Business Card

Address:
18 North Tamlin Glen Road, Unit 57, Marbrook Vale, ON, K7T 2R9
Office: 905-218-5937

Holvasters Logo
Employee Job Description
Employee Cell Phone #
Employee Email
www.holvaster-example.com

Colors

Designer to choose colors to be used in the design.

Requirements
Must have
• Quote Company Saying:
• "Professional. Quality. Service."
Nice to have
• New Crisp up to date look. simple & fresh ( Not to Busy)
Should not have
• NO BLUE PRINTS ON THE BUSINESS CARDS

```html
<!DOCTYPE html>
<html lang="en">
<head>
<meta charset="utf-8">
<title>Holvaster Building Inc. – Business Card</title>
<link rel="stylesheet" href="https://fonts.googleapis.com/css2?family=Montserrat:wght@300;400;600&display=swap">
<style>
  :root {
    --brand-green: #00665a;
    --brand-green-dark: #005a4f;
    --ink-grey: #4a4a4a;
    --paper: #ffffff;
    --backdrop: #e9e6e1;
  }
  * { box-sizing: border-box; margin: 0; padding: 0; }
  html, body { width: 1200px; height: 1200px; overflow: hidden; }
  body {
    background: var(--backdrop);
    font-family: "Montserrat", Arial, sans-serif;
    position: relative;
  }
  .card {
    position: absolute;
    left: 180px;
    width: 840px;
    height: 480px;
    box-shadow: 0 6px 18px rgba(0,0,0,0.18);
  }
  .card--front { top: 90px; background: var(--brand-green); color: var(--paper); }
  .card--back { top: 630px; background: var(--paper); }

  .wordmark { position: absolute; display: flex; align-items: center; gap: 18px; }
  .wordmark__square { width: 70px; height: 70px; flex: none; }
  .wordmark__name {
    font-weight: 600;
    font-size: 34px;
    line-height: 1.05;
    letter-spacing: 1px;
    text-transform: uppercase;
  }

  .card--front .wordmark { left: 210px; top: 170px; }
  .card--front .wordmark__square { border: 4px solid var(--paper); }
  .card--front .wordmark__name { color: var(--paper); }
  .tagline {
    position: absolute;
    left: 0; right: 0; top: 330px;
    text-align: center;
    font-weight: 300;
    font-size: 22px;
    letter-spacing: 3px;
  }

  .card--back .wordmark { left: 60px; top: 150px; }
  .card--back .wordmark__square { background: var(--brand-green); }
  .card--back .wordmark__name { color: var(--brand-green); }

  .contact { position: absolute; left: 490px; top: 60px; width: 330px; }
  .contact__name { font-weight: 600; font-size: 22px; color: var(--ink-grey); text-transform: uppercase; }
  .contact__role { font-weight: 400; font-size: 15px; color: var(--brand-green); margin-top: 4px; }
  .contact__list { list-style: none; margin-top: 100px; }
  .contact__item {
    display: flex; align-items: flex-start; gap: 8px;
    font-size: 15px; color: var(--ink-grey); margin-bottom: 4px;
  }
  .contact__item--phone { font-size: 22px; font-weight: 600; }
  .contact__icon { width: 16px; height: 16px; flex: none; margin-top: 3px; fill: var(--brand-green); }
  .contact__item--phone .contact__icon { margin-top: 6px; }
</style>
</head>
<body>
  <section class="card card--front">
    <div class="wordmark">
      <span class="wordmark__square"></span>
      <span class="wordmark__name">Holvaster<br>Building Inc.</span>
    </div>
    <p class="tagline">PROFESSIONAL. QUALITY. SERVICE.</p>
  </section>

  <section class="card card--back">
    <div class="wordmark">
      <span class="wordmark__square"></span>
      <span class="wordmark__name">Holvaster<br>Building Inc.</span>
    </div>
    <div class="contact">
      <p class="contact__name">Dale Marchetti</p>
      <p class="contact__role">CEO/Founder of eLearnly.example</p>
      <ul class="contact__list">
        <li class="contact__item contact__item--phone">
          <svg class="contact__icon" viewBox="0 0 16 16"><path d="M2 5c0-2 2-3 6-3s6 1 6 3l-3 1-1-2H6L5 6 2 5zM4 7h8l2 7H2z"/></svg>
          905-218-5937
        </li>
        <li class="contact__item contact__item--phone">
          <svg class="contact__icon" viewBox="0 0 16 16"><path d="M4 1h8v14H4zM5.5 2.5v10h5v-10z"/></svg>
          905-218-5937
        </li>
        <li class="contact__item">
          <svg class="contact__icon" viewBox="0 0 16 16"><path d="M1 4h14v9H1zM2 5l6 4 6-4"/></svg>
          dale@holvaster-example.com
        </li>
        <li class="contact__item">
          <svg class="contact__icon" viewBox="0 0 16 16"><circle cx="8" cy="8" r="7"/></svg>
          www.holvaster-example.com
        </li>
        <li class="contact__item">
          <svg class="contact__icon" viewBox="0 0 16 16"><path d="M8 1a5 5 0 0 1 5 5c0 4-5 9-5 9S3 10 3 6a5 5 0 0 1 5-5zm0 3a2 2 0 1 0 0 4 2 2 0 0 0 0-4z"/></svg>
          <span>18 North Tamlin Glen Road, Unit 57,<br>Marbrook Vale, ON, K7T 2R9</span>
        </li>
      </ul>
    </div>
  </section>
</body>
</html>
```